Design profile for MuroDeck Nordhaven

I had a logo competition here recently, and was left with two logos that I could not choose between. Therefore, I create this competition where I want a complete design package or a visual identity for the company. I want you to create design elements that can be used both in print and online. (letterhead, envelopes, business card, website, facebook, etc.) I have also attached a picture of the car I have ordered. I'm happy if you can show how the design can be used on that as well.
What is important is that the logos are treated individually, and that the design you create reflects or builds up under the logo. I want the design to be recognizable and to have a connection with the logo and what we do. (take fizzo lumo as an example. if you remove the name, but keep the red color and the white line, then you will recognize which brand it is about right away)
You choose whether you want to make proposals only for one logo, or or both, but it is important that they are treated individually. The best overall package determines which logo I use.
I have also added an image that you can use as an example background if you want it in a facebook banner for example.
It is important that the design looks professional and unique. A number of designs have come in, but many of the designs are very similar and general. Here is a video of the printer if you need inspiration: https://clipvault.example/v/Q8ZtrMx2LwK

Industry/Entity Type

WallPrinting

Requirements
Must have
• Unique an professional design that can be used both online and print
Nice to have
• Show how to use the design on a VX Tully. (see photos attached)
Should not have
• The design can be simple, but not too simple and general. I want it to give the company an identity

```html
<!DOCTYPE html>
<html lang="en">
<head>
<meta charset="utf-8">
<title>MuroDeck Nordhaven – Visual Identity</title>
<link href="https://fonts.googleapis.com/css2?family=Oswald:wght@400;500;600&family=Archivo:wght@400;700&display=swap" rel="stylesheet">
<style>
:root{
  --ink:#0a0a0a;
  --paper:#ffffff;
  --brand-blue:#0a9ad8;
  --brand-yellow:#ffe500;
  --brand-red:#e2101a;
  --board-light:#b3b6ba;
  --board-dark:#63666c;
  --window:#e2e2e2;
}
*{margin:0;padding:0;box-sizing:border-box}
html,body{width:1200px;height:1200px;overflow:hidden}
body{
  position:relative;
  background:linear-gradient(35deg,var(--board-dark) 0%,#8d9095 45%,var(--board-light) 100%);
  font-family:"Oswald",sans-serif;
  color:var(--ink);
}
.icon-defs{position:absolute;width:0;height:0}
.item-label{
  position:absolute;text-align:center;
  font-family:"Oswald",sans-serif;font-weight:600;
  font-size:21px;line-height:23px;color:var(--ink);
}
.sheet{position:absolute;background:var(--paper);box-shadow:0 3px 10px rgba(0,0,0,.25);overflow:hidden}
.sheet.dark{background:var(--ink)}
.brand-name{
  font-family:"Oswald",sans-serif;font-weight:600;color:var(--ink);
  white-space:nowrap;line-height:1;position:absolute;
}
.dark .brand-name{color:var(--paper)}
.stripes{position:absolute;left:0;right:0;bottom:0;display:flex;flex-direction:column}
.stripes i{display:block}
.stripes .s-blue{background:var(--brand-blue)}
.stripes .s-yellow{background:var(--brand-yellow)}
.stripes .s-red{background:var(--brand-red)}
.stripes .s-black{background:var(--ink)}
.icon{width:1em;height:1em;fill:none;stroke:currentColor;stroke-width:2;vertical-align:middle}

/* Letterhead */
.letterhead{left:135px;top:173px;width:284px;height:400px}
.letterhead .brand-name{left:35px;top:26px;font-size:9px}
.lh-contact{position:absolute;left:42px;top:55px;font-size:3.6px;line-height:6px;font-weight:500}
.lh-contact .icon{font-size:4px;margin-right:2px}
.lh-heading{position:absolute;left:35px;top:100px;font-family:"Archivo",sans-serif;font-weight:700;font-size:8px;color:var(--brand-red)}
.lh-body{position:absolute;left:35px;top:114px;width:216px;font-family:"Archivo",sans-serif;font-size:3.6px;line-height:5.9px}
.lh-body p{margin-bottom:5px}
.letterhead .s-blue{height:2px}.letterhead .s-yellow{height:4px}.letterhead .s-red{height:7px}.letterhead .s-black{height:11px}

/* Business card front */
.card-front{left:455px;top:175px;width:303px;height:173px}
.card-front .brand-name{left:38px;top:30px;font-size:15px}
.cf-person{position:absolute;left:37px;top:76px;font-weight:500;font-size:11.5px}
.cf-person .first{color:var(--brand-red)}
.cf-person .last{color:var(--brand-blue)}
.cf-title{position:absolute;left:37px;top:92px;font-size:8px;font-style:italic;font-weight:500}
.cf-web{position:absolute;right:28px;top:92px;font-size:8.5px;font-weight:500}
.card-front .s-blue{height:2px}.card-front .s-yellow{height:3px}.card-front .s-red{height:6px}.card-front .s-black{height:43px}
.cf-contacts{position:absolute;left:0;right:0;bottom:0;height:43px;color:var(--paper);font-size:8.5px;line-height:13px}
.cf-contacts .icon{position:absolute;font-size:15px}
.cf-contacts .text{position:absolute;top:8px}
.cf-contacts .divider{position:absolute;left:138px;top:10px;width:1px;height:20px;background:var(--paper)}

/* Business card back */
.card-back{left:781px;top:175px;width:303px;height:173px}
.card-back .brand-name{left:0;right:0;top:70px;text-align:center;font-size:31px}

/* Facebook cover */
.fb-cover{left:626px;top:471px;width:390px;height:148px}
.fb-cover .brand-name{left:0;right:0;top:50px;text-align:center;font-size:40px}

/* Notebook */
.notebook{left:132px;top:624px;width:280px;height:393px}
.notebook .brand-name{left:0;right:0;top:118px;text-align:center;font-size:21px}
.nb-spiral{position:absolute;left:126px;top:632px;width:20px;height:370px;
  background:repeating-linear-gradient(180deg,transparent 0 6px,#cfd0d2 6px 8px,#3a3a3a 8px 10px,transparent 10px 17.2px)}
.notebook .s-blue{height:2px}.notebook .s-yellow{height:4px}.notebook .s-red{height:7px}.notebook .s-black{height:12px}

/* Envelope */
.envelope{left:451px;top:704px;width:632px;height:315px}
.envelope .brand-name{left:50px;top:178px;font-size:21px}
.env-contacts{position:absolute;left:50px;top:244px;font-size:5.6px;line-height:8.5px;font-weight:500}
.env-contacts .col{position:absolute;top:0;white-space:nowrap}
.env-contacts .icon{font-size:6px;margin-right:1px}
.env-contacts .divider{position:absolute;left:68px;top:0;width:1px;height:17px;background:var(--ink)}
.env-window{position:absolute;left:281px;top:156px;width:278px;height:110px;border-radius:10px;
  background:linear-gradient(120deg,#efefef,var(--window) 60%,#d4d4d4);box-shadow:inset 0 1px 3px rgba(0,0,0,.2)}
.envelope .s-blue{height:2px}.envelope .s-yellow{height:4px}.envelope .s-red{height:8px}.envelope .s-black{height:14px}
</style>
</head>
<body>

<svg class="icon-defs" aria-hidden="true">
  <defs>
    <symbol id="i-pin" viewBox="0 0 24 24"><path d="M12 22s7-7.5 7-13a7 7 0 0 0-14 0c0 5.5 7 13 7 13z"/><circle cx="12" cy="9" r="2.6"/></symbol>
    <symbol id="i-phone" viewBox="0 0 24 24"><path d="M5 3h4l2 5-2.5 1.5a11 11 0 0 0 6 6L16 13l5 2v4a2 2 0 0 1-2 2A17 17 0 0 1 3 5a2 2 0 0 1 2-2z"/></symbol>
    <symbol id="i-mail" viewBox="0 0 24 24"><rect x="2" y="5" width="20" height="14"/><path d="M2 5l10 8 10-8"/></symbol>
    <symbol id="i-globe" viewBox="0 0 24 24"><circle cx="12" cy="12" r="9"/><path d="M3 12h18M12 3c3 3 3 15 0 18M12 3c-3 3-3 15 0 18"/></symbol>
  </defs>
</svg>

<div class="item-label" style="left:177px;top:144px;width:200px">Letterhead</div>
<div class="item-label" style="left:507px;top:121px;width:200px">Business Card<br>frontside</div>
<div class="item-label" style="left:832px;top:121px;width:200px">Business Card<br>backside</div>
<div class="item-label" style="left:682px;top:437px;width:300px">Facebook cover picture</div>
<div class="item-label" style="left:175px;top:596px;width:200px">Notebook</div>
<div class="item-label" style="left:670px;top:674px;width:200px">Envelope</div>

<section class="sheet letterhead">
  <span class="brand-name">MuroDeck Nordhaven</span>
  <div class="lh-contact">
    <div><svg class="icon"><use href="#i-phone"/></svg>phone # 123-456-7890</div>
    <div><svg class="icon"><use href="#i-pin"/></svg>1234 Streetname</div>
    <div style="padding-left:6px">City, State 123456</div>
    <div><svg class="icon"><use href="#i-globe"/></svg>WWW.WEBSITE.COM</div>
  </div>
  <h1 class="lh-heading">LOREM IPSUM DOLOR SIT AMET</h1>
  <div class="lh-body">
    <p>Thank you for choosing us for your next wall project. Our team prints murals, patterns and signage straight onto walls with fast, clean equipment that leaves no mess and lasts for years. We work in homes, offices, shops, schools and public spaces, and every print is made to order in the colours you choose. Our printer handles brick, concrete, plaster, wood and glass, so almost any surface can carry your idea. Send us a sketch or a photo and we will prepare a proof before a single drop of ink is used.</p>
    <p>Thank you for choosing us for your next wall project. Our team prints murals, patterns and signage straight onto walls with fast, clean equipment that leaves no mess and lasts for years. We work in homes, offices, shops, schools and public spaces, all year round.</p>
    <p>Thank you for choosing us for your next wall project. Our team prints murals, patterns and signage straight onto walls with fast, clean equipment that leaves no mess and lasts for years. We work in homes, offices, shops, schools and public spaces, and every print is made to order in the colours you choose. Our printer handles brick, concrete, plaster, wood and glass, so almost any surface can carry your idea. Send us a sketch or a photo and we will prepare a proof before a single drop of ink is used.</p>
    <p>Thank you for choosing us for your next wall project. Our team prints murals, patterns and signage straight onto walls with fast, clean equipment that leaves no mess and lasts for years. We work in homes, offices, shops, schools and public spaces, all year round.</p>
    <p>Thank you for choosing us for your next wall project. Our team prints murals, patterns and signage straight onto walls with fast, clean equipment that leaves no mess and lasts for years. We work in homes, offices, shops, schools and public spaces, and every print is made to order in the colours you choose. Our printer handles brick, concrete, plaster, wood and glass, so almost any surface can carry your idea. Send us a sketch or a photo and we will prepare a proof before a single drop of ink is used.</p>
    <p>Thank you for choosing us for your next wall project. Our team prints murals, patterns and signage straight onto walls with fast, clean equipment that leaves no mess and lasts for years. We work in homes, offices, shops, schools and public spaces, and every print is made to order in the colours you choose. Our printer handles brick, concrete, plaster, wood and glass, so almost any surface can carry your idea. Send us a sketch or a photo and we will prepare a proof before a single drop of ink is used.</p>
    <p>Thank you for choosing us for your next wall project. Our team prints murals, patterns and signage straight onto walls with fast, clean equipment that leaves no mess and lasts for years. We work in homes, offices, shops, schools and public spaces, and every print is made to order in the colours you choose. Our printer handles brick, concrete, plaster, wood and glass, so almost any surface can carry your idea. Send us a sketch or a photo and we will prepare a proof before a single drop of ink is used.</p>
    <p>Thank you for choosing us for your next wall project. Our team prints murals, patterns and signage straight onto walls with fast, clean equipment that lasts.</p>
  </div>
  <div class="stripes"><i class="s-blue"></i><i class="s-yellow"></i><i class="s-red"></i><i class="s-black"></i></div>
</section>

<section class="sheet card-front">
  <span class="brand-name">MuroDeck Nordhaven</span>
  <div class="cf-person"><span class="first">First Name</span> <span class="last">Last Name</span></div>
  <div class="cf-title">TITLE</div>
  <div class="cf-web">WWW.WEBSITE.COM</div>
  <div class="stripes"><i class="s-blue"></i><i class="s-yellow"></i><i class="s-red"></i><i class="s-black"></i></div>
  <div class="cf-contacts">
    <svg class="icon" style="left:38px;top:10px"><use href="#i-pin"/></svg>
    <div class="text" style="left:56px">1234 Streetname<br>City, State 123456</div>
    <span class="divider"></span>
    <svg class="icon" style="left:161px;top:5px;font-size:12px"><use href="#i-phone"/></svg>
    <svg class="icon" style="left:161px;top:19px;font-size:12px"><use href="#i-mail"/></svg>
    <div class="text" style="left:178px">123-456-7890<br>firstname@website.com</div>
  </div>
</section>

<section class="sheet dark card-back">
  <span class="brand-name">MuroDeck Nordhaven</span>
</section>

<section class="sheet dark fb-cover">
  <span class="brand-name">MuroDeck Nordhaven</span>
</section>

<section class="sheet notebook">
  <span class="brand-name">MuroDeck Nordhaven</span>
  <div class="stripes"><i class="s-blue"></i><i class="s-yellow"></i><i class="s-red"></i><i class="s-black"></i></div>
</section>
<div class="nb-spiral"></div>

<section class="sheet envelope">
  <span class="brand-name">MuroDeck Nordhaven</span>
  <div class="env-contacts">
    <div class="col" style="left:0"><svg class="icon"><use href="#i-pin"/></svg>1234 Streetname<br><span style="padding-left:8px">City, State 123456</span></div>
    <span class="divider"></span>
    <div class="col" style="left:81px"><svg class="icon"><use href="#i-phone"/></svg>phone # 123-456-7890<br><svg class="icon"><use href="#i-globe"/></svg>WWW.WEBSITE.COM</div>
  </div>
  <div class="env-window"></div>
  <div class="stripes"><i class="s-blue"></i><i class="s-yellow"></i><i class="s-red"></i><i class="s-black"></i></div>
</section>

</body>
</html>
```